MD Business Card

I want to create a simple business card.
I am a consultant. I design and develop furniture, lighting and accessories for hospitality and retail brands.
I want the card to be simple and clean. Not too much of a logo - but it needs the basic information shown on the attached file.
Also - I have shown some fonts that I like on the attached file.
The card can be square or rectangle. It should be double sided.
I prefer 1-2 colors (not too colorful - but using color an an accent) Even if using color on the edges as an accent.

My snapquilt link shows some other graphics styles that I like. I like clean and simple.
http://www.snapquilt.com/marendowsett/business-cards/

Reason: I needed a few more days to see some of the options evolve.

Hospitality

```html
<!DOCTYPE html>
<html lang="en">
<head>
<meta charset="utf-8">
<title>MD Business Card</title>
<link rel="stylesheet" href="https://fonts.googleapis.com/css2?family=Oswald:wght@300;400&display=swap">
<style>
  :root {
    --backdrop: #e9e6e1;
    --card: #f4f4f2;
    --card-shade: #ecedea;
    --ink: #8a8a8a;
    --ink-soft: #a3a3a3;
    --rule: #dcdcda;
    --accent: #e8766e;
  }
  * { margin: 0; padding: 0; box-sizing: border-box; }
  html, body { width: 1200px; height: 900px; overflow: hidden; }
  body {
    background: var(--backdrop);
    font-family: "Oswald", "Arial Narrow", sans-serif;
    font-weight: 300;
    position: relative;
  }
  .card {
    position: absolute;
    width: 640px;
    height: 366px;
    background: var(--card);
    box-shadow: 0 2px 6px rgba(0,0,0,.12);
  }
  /* contact side */
  .card--contact { left: 110px; top: 70px; }
  .contact__rule {
    position: absolute; left: 0; right: 0; height: 1px; background: var(--rule);
  }
  .contact__rule--top { top: 150px; }
  .contact__rule--bottom { top: 248px; }
  .contact__divider {
    position: absolute; left: 348px; top: 150px; width: 1px; height: 98px; background: var(--rule);
  }
  .identity {
    position: absolute; right: 310px; top: 166px; text-align: right;
  }
  .identity__name {
    font-size: 38px; letter-spacing: 2px; color: var(--ink); line-height: 1.1; text-transform: uppercase;
  }
  .identity__role {
    font-size: 17px; letter-spacing: 3px; color: var(--ink-soft); text-transform: uppercase; margin-top: 4px;
  }
  .amp { color: var(--accent); font-weight: 400; }
  .reach { position: absolute; left: 372px; top: 166px; }
  .reach__phone { font-size: 30px; letter-spacing: 2px; color: var(--ink); line-height: 1.1; }
  .reach__email { font-size: 15px; letter-spacing: 2px; color: var(--ink-soft); text-transform: uppercase; margin-top: 10px; }
  .at { color: var(--accent); }
  .contact__web {
    position: absolute; left: 0; right: 0; top: 262px; text-align: center;
    font-size: 15px; letter-spacing: 3px; color: var(--ink-soft); text-transform: uppercase;
  }
  /* name side */
  .card--name {
    left: 450px; top: 470px;
    background: linear-gradient(160deg, var(--card) 0%, var(--card) 50%, var(--card-shade) 50.2%, var(--card) 100%);
    display: flex; align-items: center; justify-content: center;
  }
  .card__wordmark {
    font-size: 38px; font-weight: 300; letter-spacing: 6px; color: var(--ink); line-height: 1;
    text-transform: uppercase;
  }
</style>
</head>
<body>
  <section class="card card--contact">
    <div class="contact__rule contact__rule--top"></div>
    <div class="contact__rule contact__rule--bottom"></div>
    <div class="contact__divider"></div>
    <div class="identity">
      <div class="identity__name">Maren Dowsett</div>
      <div class="identity__role">Hospitality <span class="amp">&amp;</span> Home</div>
    </div>
    <div class="reach">
      <div class="reach__phone">917.555.0148</div>
      <div class="reach__email">maren<span class="at">@</span>marendowsett.com</div>
    </div>
    <div class="contact__web">www.marendowsett.com</div>
  </section>

  <section class="card card--name">
    <span class="card__wordmark">MD</span>
  </section>
</body>
</html>
```